Business Card Design Project

Construction

Industry/Entity Type

Business

Contact Information for Business Card

I've had the same logo for about 5 years. The logo itself is fine, however I'm looking to get a new design on the card. The green for the log is fine but the grey for the rest of the card is kind of dark and blah. Would like a new look. I'll send the file with the logo.

```html
<!DOCTYPE html>
<html lang="en">
<head>
<meta charset="utf-8">
<title>Northline Commercial Builders – Business Card</title>
<link rel="stylesheet" href="https://fonts.googleapis.com/css2?family=Roboto:wght@400;500;700&family=Open+Sans:wght@400&family=Montserrat:wght@500&display=swap">
<style>
  :root {
    --green: #18a349;
    --green-dark: #14703a;
    --green-band: #157c3c;
    --ink: #111111;
    --paper: #ffffff;
    --edge: #cfd3d1;
  }
  * { margin: 0; padding: 0; box-sizing: border-box; }
  html, body { width: 960px; height: 1200px; overflow: hidden; background: var(--paper); }
  body { position: relative; font-family: "Roboto", Arial, sans-serif; }

  .card {
    position: absolute; left: 80px; width: 800px; height: 480px;
    background: var(--paper); overflow: hidden;
    box-shadow: -6px 8px 10px rgba(0,0,0,0.35);
  }
  .card--front { top: 82px; }
  .card--back { top: 629px; }
  .card__bg { position: absolute; inset: 0; }

  .wordmark {
    position: absolute; left: 50px; width: 268px; text-align: center;
    font-weight: 700; color: var(--ink); line-height: 1.05;
  }
  .wordmark__square {
    display: block; width: 70px; height: 70px; margin: 0 auto 14px;
    background: var(--green);
  }
  .wordmark__name { display: block; font-size: 34px; letter-spacing: 0.5px; }
  .wordmark__sub { display: block; font-size: 13.5px; letter-spacing: 1.8px; margin-top: 4px; }
  .card--front .wordmark { top: 150px; }
  .card--back .wordmark { top: 175px; }

  .license-number {
    position: absolute; top: 286px; left: 50px; width: 268px; text-align: center;
    font-family: "Open Sans", Arial, sans-serif; font-size: 18px; color: var(--ink);
  }

  .contact { position: absolute; right: 80px; text-align: right; color: var(--paper); }
  .contact__name { top: 86px; font-size: 35px; font-weight: 700; line-height: 1; }
  .contact__title { top: 127px; font-size: 23px; line-height: 1; }
  .contact__email { top: 181px; font-size: 19.5px; }
  .contact__phone { top: 208px; font-size: 27px; }
  .contact__area { top: 244px; font-size: 19px; line-height: 24px; }

  .years-badge { position: absolute; left: 556px; top: 322px; }

  .back-section { position: absolute; color: var(--paper); }
  .back-heading { font-size: 29px; font-weight: 700; line-height: 1; }
  .licenses-heading { left: 485px; top: 70px; }
  .license-list { left: 432px; top: 104px; list-style: none; font-size: 21px; line-height: 25.6px; }
  .license-list li::before { content: "•"; display: inline-block; width: 18px; font-size: 14px; vertical-align: 2px; }
  .naics-heading { left: 456px; top: 235px; }
  .naics-codes { left: 426px; top: 272px; font-size: 21px; line-height: 25.6px; }

  .cert-seal { position: absolute; top: 342px; width: 74px; height: 74px; }
  .cert-seal--a { left: 509px; }
  .cert-seal--b { left: 629px; }

  .back-phone { position: absolute; left: 68px; top: 308px; font-size: 42px; color: var(--ink); letter-spacing: 0.5px; }
  .back-web {
    position: absolute; left: 69px; top: 361px; font-family: "Montserrat", Arial, sans-serif;
    font-size: 13.5px; letter-spacing: 1.6px; color: var(--ink);
  }
  .back-fine {
    position: absolute; left: 69px; top: 383px; font-family: "Montserrat", Arial, sans-serif;
    font-size: 12px; letter-spacing: 1.6px; line-height: 17px; color: var(--ink); font-variant: small-caps;
  }
</style>
</head>
<body>

<section class="card card--front" aria-label="Business card front">
  <svg class="card__bg" width="800" height="480" viewBox="0 0 800 480" aria-hidden="true">
    <line x1="406" y1="0" x2="268" y2="480" stroke="var(--edge)" stroke-width="3"/>
    <polygon points="409,0 800,0 800,480 271,480" fill="var(--green)"/>
    <polygon points="336,246 536,480 271,480" fill="var(--green-dark)"/>
    <polygon points="398,74 800,74 800,165 376,165" fill="var(--green-band)"/>
  </svg>

  <div class="wordmark">
    <span class="wordmark__square"></span>
    <span class="wordmark__name">NORTHLINE</span>
    <span class="wordmark__sub">COMMERCIAL BUILDERS</span>
  </div>
  <p class="license-number">license#1004872</p>

  <p class="contact contact__name">Dana Reyes</p>
  <p class="contact contact__title">DMP Prestdent</p>
  <p class="contact contact__email">dana@northlinecommercial.com</p>
  <p class="contact contact__phone">(310)555-0148</p>
  <p class="contact contact__area">SERVING ALL OF<br>SOUTHERN CALIFORNIA</p>

  <svg class="years-badge" width="160" height="90" viewBox="0 0 160 90" aria-label="Over 25 years of service excellence">
    <path d="M33 36 A47 47 0 0 1 127 36" fill="none" stroke="var(--paper)" stroke-width="3"/>
    <text x="80" y="34" text-anchor="middle" font-family="Roboto, Arial, sans-serif" font-size="18" fill="var(--paper)">OVER</text>
    <polygon points="0,38 160,38 152,52 160,66 0,66 8,52" fill="var(--paper)"/>
    <text x="82" y="62" text-anchor="middle" font-family="Roboto, Arial, sans-serif" font-weight="700" font-size="24" fill="var(--green)">25YEARS</text>
    <text x="78" y="84" text-anchor="middle" font-family="Roboto, Arial, sans-serif" font-size="12.5" fill="var(--paper)">OF SERVICE EXCELLENCE</text>
  </svg>
</section>

<section class="card card--back" aria-label="Business card back">
  <svg class="card__bg" width="800" height="480" viewBox="0 0 800 480" aria-hidden="true">
    <line x1="437" y1="0" x2="299" y2="480" stroke="var(--edge)" stroke-width="3"/>
    <polygon points="440,0 800,0 800,480 302,480" fill="var(--green)"/>
    <polygon points="360,271 536,480 302,480" fill="var(--green-dark)"/>
  </svg>

  <div class="wordmark">
    <span class="wordmark__square"></span>
    <span class="wordmark__name">NORTHLINE</span>
    <span class="wordmark__sub">COMMERCIAL BUILDERS</span>
  </div>

  <p class="back-phone">310.555.0148</p>
  <p class="back-web">NORTHLINECOMMERCIAL.COM</p>
  <p class="back-fine">Licensed, bonded, insured<br>License #708215</p>

  <h2 class="back-section back-heading licenses-heading">LICENSES</h2>
  <ul class="back-section license-list">
    <li>A &nbsp;&nbsp;&nbsp;- General Engineering</li>
    <li>B &nbsp;&nbsp;&nbsp;- General Building</li>
    <li>C12- Demo / Bldg.movimh</li>
    <li>C36- Plombing</li>
  </ul>

  <h2 class="back-section back-heading naics-heading">NAICS CODES</h2>
  <p class="back-section naics-codes">236220, 238110, 236118<br>23810, 238350. 238390, 327320</p>

  <svg class="cert-seal cert-seal--a" viewBox="0 0 74 74" role="img" aria-label="Certification seal">
    <circle cx="37" cy="37" r="36" fill="var(--ink)"/>
    <circle cx="37" cy="37" r="29" fill="none" stroke="var(--paper)" stroke-width="1.5"/>
  </svg>
  <svg class="cert-seal cert-seal--b" viewBox="0 0 74 74" role="img" aria-label="Certification seal">
    <circle cx="37" cy="37" r="36" fill="var(--ink)"/>
    <circle cx="37" cy="37" r="29" fill="none" stroke="var(--paper)" stroke-width="1.5"/>
  </svg>
</section>

</body>
</html>
```